Please design a business card with my current logo (attached below).

I have some specifics that must be included:
1. I want the emphasis on Licensed Heritage Home Transfer Consultant.
2. Leave room for my picture.
3. Company name, address, phone numbers and email address.
4. My BRE# should be placed under my name.

```html
<!DOCTYPE html>
<html lang="en">
<head>
<meta charset="utf-8">
<title>Mara Dalton – Business Card</title>
<link rel="stylesheet" href="https://fonts.googleapis.com/css2?family=Open+Sans:wght@400;600;700&display=swap">
<style>
  :root {
    --backdrop: #e8e5e0;
    --charcoal-light: #3d3d3f;
    --charcoal-dark: #262627;
    --brand-red: #b5141d;
    --brand-red-dark: #8e0f16;
    --paper: #f3f3f3;
    --text-light: #ffffff;
    --text-muted: #d6d6d6;
    --photo-frame: #151515;
  }
  * { box-sizing: border-box; margin: 0; padding: 0; }
  html, body { width: 1200px; height: 1000px; overflow: hidden; }
  body {
    background: var(--backdrop);
    font-family: "Open Sans", Arial, sans-serif;
    position: relative;
  }
  .card {
    position: absolute;
    left: 215px;
    width: 770px;
    height: 440px;
    overflow: hidden;
    background: linear-gradient(135deg, var(--charcoal-light), var(--charcoal-dark));
    box-shadow: 0 6px 18px rgba(0,0,0,0.18);
  }
  .card-back { top: 40px; }
  .card-front { top: 520px; }

  /* Back */
  .back-brand {
    position: absolute;
    inset: 0;
    display: flex;
    align-items: center;
    justify-content: center;
    gap: 28px;
  }
  .brand-square {
    background: var(--brand-red);
    flex: none;
  }
  .back-brand .brand-square { width: 84px; height: 84px; }
  .back-brand .brand-name {
    color: var(--text-light);
    font-weight: 600;
    font-size: 64px;
    letter-spacing: 4px;
    text-transform: uppercase;
    white-space: nowrap;
  }

  /* Front */
  .front-brand {
    position: absolute;
    left: 48px;
    top: 120px;
    width: 320px;
  }
  .front-brand .brand-row { display: flex; align-items: center; gap: 14px; }
  .front-brand .brand-square { width: 40px; height: 40px; }
  .front-brand .brand-name {
    color: var(--text-light);
    font-weight: 600;
    font-size: 30px;
    letter-spacing: 2px;
    text-transform: uppercase;
    white-space: nowrap;
  }
  .address {
    margin-top: 16px;
    color: var(--text-muted);
    font-size: 16px;
    line-height: 1.35;
    font-weight: 600;
  }
  .bre-strip {
    position: absolute;
    right: 0; top: 0;
    width: 64px; height: 100%;
    background: linear-gradient(180deg, var(--brand-red), var(--brand-red-dark));
  }
  .bre-number {
    position: absolute;
    right: 22px;
    top: 40px;
    writing-mode: vertical-rl;
    color: var(--text-light);
    font-size: 13px;
    font-weight: 700;
    white-space: nowrap;
  }
  .agent-photo {
    position: absolute;
    right: 74px;
    top: 22px;
    width: 300px;
    height: 210px;
    border: 5px solid var(--photo-frame);
    background: linear-gradient(180deg, #f6f6f6 0%, #e2e2e2 55%, #2b2b2b 56%, #1e1e1e 100%);
  }
  .agent-name {
    position: absolute;
    right: 80px;
    top: 244px;
    color: var(--text-light);
    font-weight: 700;
    font-size: 30px;
    white-space: nowrap;
  }
  .tagline-band {
    position: absolute;
    left: 280px;
    right: 64px;
    top: 294px;
    height: 36px;
    background: var(--paper);
    display: flex;
    align-items: center;
    justify-content: flex-end;
    padding-right: 16px;
  }
  .tagline {
    color: var(--brand-red);
    font-weight: 700;
    font-size: 13px;
    text-transform: uppercase;
    letter-spacing: 0.2px;
    white-space: nowrap;
  }
  .contact-band {
    position: absolute;
    left: 390px;
    right: 0;
    top: 330px;
    bottom: 0;
    background: linear-gradient(180deg, var(--brand-red), var(--brand-red-dark));
    padding: 20px 0 0 24px;
  }
  .contact-line {
    display: flex;
    align-items: center;
    gap: 12px;
    color: var(--text-light);
    font-weight: 600;
    font-size: 17px;
    margin-bottom: 12px;
    white-space: nowrap;
  }
  .contact-icon { width: 20px; height: 20px; flex: none; }
</style>
</head>
<body>
  <section class="card card-back" aria-label="Business card, back">
    <div class="back-brand">
      <span class="brand-square"></span>
      <span class="brand-name">Mara Dalton</span>
    </div>
  </section>

  <section class="card card-front" aria-label="Business card, front">
    <div class="front-brand">
      <div class="brand-row">
        <span class="brand-square"></span>
        <span class="brand-name">Mara Dalton</span>
      </div>
      <p class="address">2207 Lantern Ridge Rd.<br>Harbor County, CA 95021</p>
    </div>

    <div class="agent-photo" role="img" aria-label="Portrait photo of the agent"></div>

    <div class="bre-strip"></div>
    <p class="bre-number">BRE No. 4082 61937</p>

    <h1 class="agent-name">Mara Dalton</h1>

    <div class="tagline-band">
      <p class="tagline">Licensed Heritage Home Transfer Consultant</p>
    </div>

    <div class="contact-band">
      <p class="contact-line">
        <svg class="contact-icon" viewBox="0 0 20 20" aria-hidden="true">
          <rect x="5" y="1.5" width="10" height="17" rx="2" fill="none" stroke="#fff" stroke-width="1.8"/>
          <circle cx="10" cy="15.5" r="1" fill="#fff"/>
        </svg>
        (555) 410-2738 / (555) 382-904716
      </p>
      <p class="contact-line">
        <svg class="contact-icon" viewBox="0 0 20 20" aria-hidden="true">
          <rect x="1.5" y="4" width="17" height="12" fill="none" stroke="#fff" stroke-width="1.8"/>
          <path d="M1.5 4 L10 11 L18.5 4" fill="none" stroke="#fff" stroke-width="1.8"/>
        </svg>
        hello@maradalton.com
      </p>
    </div>
  </section>
</body>
</html>
```